Networking card

I just need a simple design with the following information:
Ravin Doshu
318.647.2094
rdoshu583016@mailvanta.com

I would like to have a white background with blue text like in this sample: https://cardmintly.com/business-card-207346/

```html
<!DOCTYPE html>
<html lang="en">
<head>
<meta charset="utf-8">
<title>Ravin Doshu — Networking Card</title>
<link rel="stylesheet" href="https://fonts.googleapis.com/css2?family=Montserrat:wght@400;700&display=swap">
<style>
  :root {
    --stage: #e9ebee;
    --card: #ffffff;
    --brand-blue: #0d4a85;
    --ink: #1c1c1c;
    --card-shadow: rgba(0, 0, 0, 0.18);
  }
  html, body {
    margin: 0;
    width: 1200px;
    height: 1200px;
    overflow: hidden;
    background: var(--stage);
  }
  .stage {
    width: 1200px;
    height: 1200px;
    display: flex;
    align-items: center;
    justify-content: center;
  }
  .business-card {
    position: relative;
    width: 1000px;
    height: 571px;
    background: var(--card);
    border-radius: 44px;
    border-bottom: 6px solid var(--brand-blue);
    box-shadow: 0 18px 40px var(--card-shadow);
    box-sizing: border-box;
    font-family: "Montserrat", sans-serif;
  }
  .card-content {
    position: absolute;
    left: 250px;
    top: 190px;
  }
  .holder-name {
    margin: 0 0 34px;
    color: var(--brand-blue);
    font-weight: 700;
    font-size: 62px;
    letter-spacing: 1px;
    line-height: 1;
    text-transform: uppercase;
  }
  .contact-list {
    list-style: none;
    margin: 0;
    padding: 0;
  }
  .contact-item {
    display: flex;
    align-items: center;
    gap: 16px;
    color: var(--ink);
    font-weight: 400;
    font-size: 36px;
    line-height: 1;
    margin-bottom: 18px;
  }
  .contact-icon {
    width: 44px;
    height: 44px;
    flex: none;
  }
</style>
</head>
<body>
<main class="stage">
  <article class="business-card">
    <div class="card-content">
      <h1 class="holder-name">Ravin Doshu</h1>
      <ul class="contact-list">
        <li class="contact-item">
          <svg class="contact-icon" viewBox="0 0 44 44" aria-hidden="true">
            <circle cx="22" cy="22" r="22" fill="var(--brand-blue)"/>
            <path d="M15 13c1-1 2.5-1 3.3.2l2 3c.6.9.4 2-.4 2.6l-1.3 1c.9 2.2 2.6 3.9 4.8 4.8l1-1.3c.6-.8 1.7-1 2.6-.4l3 2c1.2.8 1.2 2.3.2 3.3l-1.5 1.5c-1.6 1.6-9 -.5-12.6-4.1S11.9 17.6 13.5 14.5z" fill="#fff"/>
          </svg>
          <span>318.647.2094</span>
        </li>
        <li class="contact-item">
          <svg class="contact-icon" viewBox="0 0 44 44" aria-hidden="true">
            <circle cx="22" cy="22" r="22" fill="var(--brand-blue)"/>
            <rect x="11" y="14" width="22" height="16" rx="1.5" fill="#fff"/>
            <path d="M11.5 14.8 22 23l10.5-8.2M11.5 29.2l8-7M32.5 29.2l-8-7" fill="none" stroke="var(--brand-blue)" stroke-width="1.6"/>
          </svg>
          <span>rdoshu583016@mailvanta.com</span>
        </li>
      </ul>
    </div>
  </article>
</main>
</body>
</html>
```